A new Blog: Paper Lanterns Rising

I need a wordpress blog design for my new blog called Paper Lanterns Rising.

I'm not an alcoholic. I certainly don't think I am, and I'm fairly certain that if you spoke to my friends and family they would agree that I don't have any issues with substance abuse. I definitely enjoy a drink. A few beers, gin and tonic's or a nice red wine (along with a few cigarettes) have been particular vices for the last few years of my life.

But no more. I'm going 365 with no alcohol and I am giving up cigarettes.

Why? I have my reasons... and this blog will reveal those and chronicle my year long journey.

The blog is called Paper Lanterns Rising and I want a clean, crisp design to reflect this new adventure.

I'm looking for a design that is unique and not the same as every other blog you see. I want my readers to feel uplifted when they see it.

Most importantly, the blog needs to be simple for me to use and modify (add a new page if needed in the future)

Reason: To allow time for designers to submit revised designs.

Reason: My apologies designers, I haven't had an opportunity to provide feedback to enable changes. I will be doign this tomorrow morning and so am extending the deadline to allow resubmission.

Regards, Marek.

Target Market(s)

My target market are males and females, 17-28 in western speaking countries

Requirements
Must have
• - A graphic banner/branding featuring the blog title. This should be able to be used as a small stand alone logo.
- Ability to show my latest tweets
- A connect box where people can click on Chatterly, Quibblo and Postvox links to contact me
- A widget that is showing how many days I am into the 365 day challenge (this should feature prominently)
- A widget that shows how much money as the challenge progresses
- It should have an ability to subcribe to the blog (RSS feeds)
- There needs to be an about me page
- There should be a blog roll
- There should be a list of categories/tags displayed somewhere (do something creative with this, find a way to make what I am talking about most more prominent!)
- A recent post link box somewhere at the side to encourage people to keep reading
- Recent comment links
- A search functionality
- An advertisement side bar (only a small amount of advertising will be done - so don't make it too prominent!)

Nice to have
• Without crowding the design it would also be good to have
-Popular post links (the most highly trafficked or commented) posts.

I'm excited to hear what other things YOU THINK should feature. Surprise me! I will reward innovation.

```html
<!DOCTYPE html>
<html lang="en">
<head>
<meta charset="utf-8">
<title>Paper Lanterns Rising</title>
<link href="https://fonts.googleapis.com/css2?family=Arimo:ital,wght@0,400;0,700;1,400&family=Kalam&display=swap" rel="stylesheet">
<style>
:root{
  --ink:#1a1a1a;
  --header:#2e2b29;
  --sky-top:#b3e3f2;
  --sky-mid:#2f8dc6;
  --sky-deep:#0b5394;
  --panel:#ffffff;
  --side:#f2f2f2;
  --rule:#d6d6d6;
  --muted:#8a8a8a;
  --text:#555555;
  --green:#7cb82f;
  --link-green:#8ab04a;
  --counter:#2a2a2a;
  --splash:#1e7fd8;
}
*{margin:0;padding:0;box-sizing:border-box}
html,body{width:1200px;height:1109px;overflow:hidden;background:#fff;font-family:"Arimo",Arial,sans-serif;color:var(--text)}
.site{position:absolute;left:216px;top:0;width:768px;height:1109px;
  background:linear-gradient(180deg,var(--sky-top) 50px,#8fd2ea 150px,var(--sky-mid) 480px,var(--sky-deep) 730px,var(--sky-deep) 100%);overflow:hidden}
.topbar{position:absolute;left:0;top:0;width:768px;height:58px}
.nav{position:absolute;top:14px;left:396px;display:flex;gap:0;font-family:"Kalam",cursive;font-size:15px;color:#fff}
.nav a{color:#fff;text-decoration:none;display:block;padding:2px 14px}
.nav .current{background:var(--splash);border-radius:14px/10px}
.hero-figure{position:absolute;left:20px;top:60px;width:250px;height:340px;border-radius:50% 40% 30% 30%/30% 30% 20% 20%;
  background:radial-gradient(ellipse at 40% 40%,rgba(10,30,60,.55),rgba(10,30,60,0) 70%)}
.brand{position:absolute;left:360px;top:92px;display:flex;align-items:center;gap:8px}
.brand-mark{width:36px;height:36px;border-radius:50%;background:var(--splash)}
.brand-name{font-size:24px;color:var(--ink);font-weight:400}
.join{position:absolute;left:671px;top:128px;font-family:"Kalam",cursive;font-size:10px;color:#555}
.join-arrow{position:absolute;left:690px;top:144px}
.social{position:absolute;left:671px;top:186px;display:flex;flex-direction:column;gap:6px}
.social a{display:block;width:60px;padding:8px 4px;font-size:9px;color:#fff;background:rgba(255,255,255,.28);text-decoration:none;text-align:center}
.page{position:absolute;left:94px;top:164px;width:576px;height:893px;background:var(--panel);display:flex}
.main{width:410px;padding:24px 20px 0 20px;position:relative}
.side{width:166px;background:var(--side);padding:24px 12px 0 12px;position:relative}
.post-title{font-size:13px;font-weight:400;color:var(--ink)}
.post-meta{font-size:7.5px;color:var(--text);margin-top:3px}
.post-meta b{font-weight:400;color:var(--ink)}
.count-bubble{position:absolute;left:359px;top:26px;width:34px;height:21px}
.quote{margin-top:14px;background:#eeeeee;padding:12px 30px 12px 29px;font-size:8px;line-height:13px;position:relative;height:52px}
.quote:before{content:"\201C";position:absolute;left:11px;top:6px;font-size:20px;color:#333;font-family:Georgia,serif}
.body-text{margin-top:10px;font-size:8px;line-height:12.5px}
.body-text p{margin-bottom:4px}
.post-photo{margin-top:12px;width:378px;height:176px;border:2px solid #eee;background:linear-gradient(90deg,#a36b52 0%,#2a1d1b 22%,#0c1020 50%,#14213f 100%)}
.respond{margin-top:24px;font-size:18px;color:var(--ink);font-weight:400}
.field{margin-top:7px;display:flex;height:30px;width:228px;border:1px solid #222}
.field .ico{width:30px;background:var(--ink);display:flex;align-items:center;justify-content:center}
.field span{font-style:italic;font-size:12px;color:#444;padding:6px 7px}
.comment{margin-top:7px;width:276px;height:118px;border:1px solid #222;font-style:italic;font-size:12px;color:#444;padding:6px 7px}
.send{margin-top:6px;width:73px;height:30px;background:var(--ink);color:#fff;font-size:17px;display:flex;align-items:center;justify-content:center}
.search{height:24px;border:1px solid #d8d8d8;background:#fff;position:relative}
.search svg{position:absolute;right:6px;top:6px}
.side-rule{border-top:1px solid #cfcfcf;margin:14px 0 10px}
.widget-head{font-size:11px;color:var(--muted);text-transform:uppercase}
.days{display:flex;gap:2px;margin-top:6px}
.days div{width:34px;height:33px;background:linear-gradient(180deg,#444 0 50%,#1e1e1e 50%);border-radius:3px;color:#fff;font-size:26px;font-weight:700;display:flex;align-items:center;justify-content:center}
.equal{font-size:11px;color:var(--muted);margin-top:8px}
.money{display:flex;align-items:center;gap:2px;margin-top:3px;font-size:20px;color:#333;font-weight:700}
.money .d{width:20px;height:22px;background:var(--green);border-radius:2px;color:#fff;font-size:18px;display:flex;align-items:center;justify-content:center}
.tabs{margin-top:12px;border:1px solid #cfcfcf;background:#fff}
.tabs .bar{display:flex;font-size:9.5px;font-weight:700}
.tabs .bar span{flex:1;height:18px;display:flex;align-items:center;justify-content:center;color:#bbb;background:#f2f2f2}
.tabs .bar .on{background:#bdbdbd;color:#fff}
.tabs ul{list-style:none;padding:2px 5px 3px}
.tabs li{font-size:7.5px;color:#999;height:16px;line-height:16px;border-bottom:1px dotted #ccc}
.tabs li:last-child{border:0}
.section-head{font-size:10px;font-weight:700;color:#777;margin-top:14px}
.rc{margin-top:6px;border:1px solid #d4d4d4;background:#fff;height:40px;display:flex;gap:6px;padding:6px}
.rc .avatar{width:26px;height:26px;background:linear-gradient(180deg,#c8c8c8,#6f6f6f)}
.rc p{font-size:7px;line-height:9px;color:#aaa}
.rc p b{font-weight:400;color:var(--link-green);font-size:7.5px}
.rc p small{font-size:5.5px;color:#888}
.blogroll{list-style:none;margin-top:4px}
.blogroll li{font-size:7.5px;color:#888;height:18px;line-height:17px;border-bottom:1px dotted #ccc}
.tweet{margin-top:18px;border:1px solid #d4d4d4;border-radius:6px;background:#fff;padding:9px 8px;font-size:7.5px;line-height:11.5px;color:#444;height:87px}
.tweet small{color:#999;font-size:7.5px}
.tweet-bird{position:absolute;left:110px;top:648px;width:30px;height:36px;border-radius:50%;background:radial-gradient(circle at 50% 40%,#5fc3f0,#1c8fd3)}
.bird-shadow{position:absolute;left:70px;top:684px;width:80px;height:4px;border-radius:50%;background:rgba(0,0,0,.15)}
.ad{position:absolute;left:13px;top:705px;width:140px;height:114px;background:#fff;border:2px solid #e6e6e6;display:flex;align-items:center;justify-content:center;font-size:13px;color:#777}
.rss{position:absolute;left:32px;top:835px;width:97px;height:29px;border-radius:15px;background:#efe9e1;border:1px solid #ddd;display:flex;align-items:center;gap:10px;padding-left:2px;font-size:13px;color:#8a4d18}
.rss i{width:26px;height:26px;border-radius:50%;background:#c97a2a;display:block}
.footer{position:absolute;left:0;top:1066px;width:768px;text-align:center;font-size:8px;line-height:10px;color:#fff}
</style>
</head>
<body>
<div class="site">
  <svg class="topbar" viewBox="0 0 768 58" width="768" height="58" aria-hidden="true">
    <path d="M0 0H768V52 L763 57 L758 52 L753 57 L748 52 L743 57 L738 52 L733 57 L728 52 L723 57 L718 52 L713 57 L708 52 L703 57 L698 52 L693 57 L688 52 L683 57 L678 52 L673 57 L668 52 L663 57 L658 52 L653 57 L648 52 L643 57 L638 52 L633 57 L628 52 L623 57 L618 52 L613 57 L608 52 L603 57 L598 52 L593 57 L588 52 L583 57 L578 52 L573 57 L568 52 L563 57 L558 52 L553 57 L548 52 L543 57 L538 52 L533 57 L528 52 L523 57 L518 52 L513 57 L508 52 L503 57 L498 52 L493 57 L488 52 L483 57 L478 52 L473 57 L468 52 L463 57 L458 52 L453 57 L448 52 L443 57 L438 52 L433 57 L428 52 L423 57 L418 52 L413 57 L408 52 L403 57 L398 52 L393 57 L388 52 L383 57 L378 52 L373 57 L368 52 L363 57 L358 52 L353 57 L348 52 L343 57 L338 52 L333 57 L328 52 L323 57 L318 52 L313 57 L308 52 L303 57 L298 52 L293 57 L288 52 L283 57 L278 52 L273 57 L268 52 L263 57 L258 52 L253 57 L248 52 L243 57 L238 52 L233 57 L228 52 L223 57 L218 52 L213 57 L208 52 L203 57 L198 52 L193 57 L188 52 L183 57 L178 52 L173 57 L168 52 L163 57 L158 52 L153 57 L148 52 L143 57 L138 52 L133 57 L128 52 L123 57 L118 52 L113 57 L108 52 L103 57 L98 52 L93 57 L88 52 L83 57 L78 52 L73 57 L68 52 L63 57 L58 52 L53 57 L48 52 L43 57 L38 52 L33 57 L28 52 L23 57 L18 52 L13 57 L8 52 L3 57 L0 54Z" fill="var(--header)"/>
  </svg>
  <nav class="nav"><a class="current" href="#">Home</a><a href="#">About</a><a href="#">Contact Me</a></nav>
  <div class="hero-figure" role="img" aria-label="Silhouette of a person leaping with arms outstretched against blue light streaks"></div>
  <div class="brand"><span class="brand-mark"></span><span class="brand-name">Paper Lanterns Rising</span></div>
  <div class="join">join &nbsp;me &nbsp;on</div>
  <svg class="join-arrow" width="16" height="36" viewBox="0 0 16 36" aria-hidden="true"><path d="M12 1 C10 14 8 24 5 33 M1 27 L5 33 L9 28" fill="none" stroke="#666" stroke-width="1.2"/></svg>
  <div class="social"><a href="#">Chatterly</a><a href="#">Quibblo</a><a href="#">Postvox</a></div>

  <div class="page">
    <main class="main">
      <h1 class="post-title">Dangerous Effects of Cigarette Smoking</h1>
      <div class="post-meta">in <b>Smoking</b> tagged <b>Health</b>, <b>Bad Habit</b> on Nov 24th, 2009</div>
      <svg class="count-bubble" viewBox="0 0 34 21" aria-label="10 comments"><path d="M17 1C26 1 33 4 33 9.5S26 18 17 18L11 21 12 17C5 16 1 13 1 9.5 1 4 8 1 17 1Z" fill="var(--ink)"/><text x="17" y="12.5" text-anchor="middle" font-size="8" font-weight="700" fill="#fff" font-family="Arimo,sans-serif">10</text></svg>
      <blockquote class="quote">People who smoke a pack a day die on average 7 years earlier than people who have never smoked.</blockquote>
      <div class="body-text">
        <p>Cigarette Smoking means you are giving to yourself a slow poison treatment. Cigarette smoking does not only affect the smoker's health but also affects the nearby standing individual like your kids as their organs are on developing stage.</p>
        <p>Some people are under false impression and take cigarette smoking as a hobby. According to recent studies conducted by NHC, Northfield Wellness Society and the Open Air Heart Council, cigarette smoking is one of the main causes of premature death.</p>
      </div>
      <div class="post-photo" role="img" aria-label="Close-up photo of scissors cutting a cigarette held between lips, smoke drifting on a dark background"></div>
      <h2 class="respond">What Do You Think?</h2>
      <div class="field"><div class="ico"><svg width="18" height="18" viewBox="0 0 18 18"><circle cx="9" cy="9" r="7.5" fill="none" stroke="#fff" stroke-width="1.5"/><circle cx="6.5" cy="7" r="1" fill="#fff"/><circle cx="11.5" cy="7" r="1" fill="#fff"/><path d="M5.5 10.5Q9 14 12.5 10.5" fill="none" stroke="#fff" stroke-width="1.3"/></svg></div><span>your name</span></div>
      <div class="field"><div class="ico"><svg width="18" height="14" viewBox="0 0 18 14"><rect x="1" y="1" width="16" height="12" fill="none" stroke="#fff" stroke-width="1.3"/><path d="M1 1L9 8 17 1M1 13L7 7M17 13L11 7" fill="none" stroke="#fff" stroke-width="1.2"/></svg></div><span>e-mail</span></div>
      <div class="field"><div class="ico"><svg width="18" height="18" viewBox="0 0 18 18"><circle cx="9" cy="9" r="7.5" fill="none" stroke="#fff" stroke-width="1.3"/><ellipse cx="9" cy="9" rx="3.5" ry="7.5" fill="none" stroke="#fff" stroke-width="1"/><path d="M1.5 9H16.5M3 5H15M3 13H15" stroke="#fff" stroke-width="1"/></svg></div><span>web</span></div>
      <div class="comment">comment</div>
      <div class="send">SEND</div>
    </main>

    <aside class="side">
      <div class="search"><svg width="10" height="10" viewBox="0 0 10 10"><circle cx="4" cy="4" r="3" fill="none" stroke="#aaa" stroke-width="1.3"/><path d="M6.3 6.3L9 9" stroke="#aaa" stroke-width="1.5"/></svg></div>
      <div class="side-rule"></div>
      <div class="widget-head">Days without alcohol</div>
      <div class="days"><div>3</div><div>6</div><div>5</div></div>
      <div class="equal">Equal with</div>
      <div class="money">$<span class="d">2</span><span class="d">0</span><span class="d">5</span>.<span class="d">5</span></div>
      <div class="side-rule" style="margin:12px 0 0"></div>
      <div class="tabs">
        <div class="bar"><span>Popular Post</span><span class="on">Recent Post</span></div>
        <ul><li>Say no to smoking</li><li>Making life more healthy</li><li>Say no to smoking</li><li>Making life more healthy</li><li>Say no to smoking</li><li>Making life more healthy</li></ul>
      </div>
      <div class="section-head">Recent Comments</div>
      <div class="rc"><div class="avatar" role="img" aria-label="Commenter avatar"></div><p><b>Re: Say no to smoking</b><br>I agree with you dude...<br><small>Posted on 01-01-2010</small></p></div>
      <div class="rc"><div class="avatar" role="img" aria-label="Commenter avatar"></div><p><b>Re: Say no to smoking</b><br>I agree with you dude...<br><small>Posted on 01-01-2010</small></p></div>
      <div class="section-head">Blogroll</div>
      <ul class="blogroll"><li>Healthy Life</li><li>Health Magazine</li><li>Healthy Life</li><li>Health Magazine</li><li>Healthy Life</li></ul>
      <div class="tweet">About to embark on a browser testing adventure, but I need to get some damn coffee brewing first. What a way to end the week. Have fun everybody...<br><small>1 hr ago</small></div>
      <div class="bird-shadow"></div>
      <div class="tweet-bird" role="img" aria-label="Small blue cartoon bird beside the latest post"></div>
      <div class="ad">ADVERTISEMENT</div>
      <div class="rss"><i></i>rss feed</div>
    </aside>
  </div>

  <footer class="footer">copyright (c) www.paperlanternsrising.com 2011<br>allrights reserved</footer>
</div>
</body>
</html>
```